Business card design for Velluto Events, and Event & Entertainment business

The business card design is for a new business venture, Velluto Events. This company offers Event management, entertainment management and also Latin dance tuition. We currently run Latin dance festivals in Australia & also teach street Latin. This business card is for the director, Mara Dunhill. The Logo has already been designed. So, I need the new design to incorporate and go with the existing Logo.

The look I like is clean, simple & elegant but I also want it to be sexy. Elegant, but not corporate. Clean & simple but not boring :-)

If you want to add another design element as well as using the Logo, please use something with movement. I like ripples or swirls for example.

I would also like to have part of the card embossed or Spot UV pressed so I would like some part of the design to have texture.

Text for the Cards is as follows;

Velluto Events ( Logo attached )

Mara Dunhill

EVENTS & ENTERTAINMENT MANAGEMENT

m: 0478 352 601
e: mara@vellutoevents.com.au
f Velluto Events

www.vellutoevents.com.au

Please try portrait layout.

Thanks, Mara
Updates

Hello Designers, Thank you to all of you who have submitted designs for Velluto Events. I will make up my mind now from what I have already been sent. Very close to making a decision :-) Thank you, Mara

Target Market(s)

Adults, 18 - 60 age group. People who are active. People interested in different cultures. People who like to travel. Please who like to have fun. People who are passionate about Latin dance.

Industry/Entity Type

Entertainment

Font styles to use
Sans Serif
Script

Colors
9bcb3c
ec1f27
ffffff

Requirements
Must have
• Logo + All text listed in brief
Nice to have
• An extra design feature or background image that could be embossed or spot uv pressed to add texture & flare.

```html
<!DOCTYPE html>
<html lang="en">
<head>
<meta charset="utf-8">
<title>Velluto Events – Business Card</title>
<link rel="stylesheet" href="https://fonts.googleapis.com/css2?family=Open+Sans:wght@400;600&display=swap">
<style>
  :root {
    --backdrop: #e7e4e1;
    --card-red: #ec1f27;
    --card-black: #141414;
    --brand-grey: #3a3a3a;
    --brand-grey-soft: #4a4a4a;
    --accent-green: #9bcb3c;
    --name-red: #d4242b;
    --white: #ffffff;
  }
  * { margin: 0; padding: 0; box-sizing: border-box; }
  html, body {
    width: 1200px; height: 827px; overflow: hidden;
    background: var(--backdrop);
    font-family: "Open Sans", Arial, sans-serif;
  }
  .stage {
    position: relative; width: 1200px; height: 827px;
    display: flex; align-items: center; justify-content: center; gap: 40px;
  }
  .card {
    position: relative; width: 540px; height: 310px;
    box-shadow: 0 10px 28px rgba(0,0,0,0.18);
  }

  /* Front */
  .card--front { background: var(--card-red); }
  .front-brand {
    position: absolute; left: 58px; top: 96px;
    display: flex; align-items: center; gap: 14px;
  }
  .brand-dot {
    width: 26px; height: 26px; border-radius: 50%;
    background: var(--accent-green);
  }
  .brand-name {
    font-weight: 600; font-size: 44px; letter-spacing: 0.5px;
    color: var(--brand-grey);
  }
  .front-tagline {
    position: absolute; left: 58px; top: 176px;
    font-size: 15px; letter-spacing: 1px; color: var(--white);
  }

  /* Back */
  .card--back { background: var(--card-black); }
  .back-brand {
    position: absolute; left: 34px; top: 128px;
    display: flex; align-items: center; gap: 10px;
  }
  .back-brand .brand-name { font-size: 30px; color: var(--brand-grey-soft); }
  .back-brand .brand-dot { width: 18px; height: 18px; }
  .divider {
    position: absolute; left: 290px; top: 92px; width: 1px; height: 120px;
    background: linear-gradient(var(--card-red), rgba(236,31,39,0));
  }
  .contact {
    position: absolute; left: 304px; top: 92px;
    list-style: none; color: var(--white); font-size: 15px; line-height: 22px;
  }
  .contact-name {
    color: var(--name-red); font-weight: 600; font-size: 18px;
    margin-bottom: 6px; padding-left: 6px;
  }
  .contact li { display: flex; align-items: center; gap: 8px; }
  .contact svg { width: 14px; height: 14px; flex: none; }
  .contact .social { margin-top: 10px; }
  .social-square { width: 12px; height: 12px; background: var(--card-red); flex: none; }
</style>
</head>
<body>
<main class="stage">
  <section class="card card--front" aria-label="Card front">
    <div class="front-brand">
      <span class="brand-dot"></span>
      <span class="brand-name">Velluto Events</span>
    </div>
    <p class="front-tagline">EVENTS &amp; ENTERTAINMENT MANAGEMENT</p>
  </section>

  <section class="card card--back" aria-label="Card back">
    <div class="back-brand">
      <span class="brand-dot"></span>
      <span class="brand-name">Velluto Events</span>
    </div>
    <span class="divider"></span>
    <ul class="contact">
      <li class="contact-name">Mara Dunhill</li>
      <li>
        <svg viewBox="0 0 14 14" aria-hidden="true"><rect x="3.5" y="1" width="7" height="12" rx="1.5" fill="none" stroke="#ec1f27" stroke-width="1.4"/><circle cx="7" cy="11" r="0.8" fill="#ec1f27"/></svg>
        0478 352 601
      </li>
      <li>
        <svg viewBox="0 0 14 14" aria-hidden="true"><rect x="1" y="3" width="12" height="8" fill="#ec1f27"/><path d="M1 3 L7 8 L13 3" fill="none" stroke="#141414" stroke-width="1.2"/></svg>
        mara@vellutoevents.com.au
      </li>
      <li>
        <svg viewBox="0 0 14 14" aria-hidden="true"><circle cx="7" cy="7" r="5.5" fill="none" stroke="#ec1f27" stroke-width="1.2"/><ellipse cx="7" cy="7" rx="2.4" ry="5.5" fill="none" stroke="#ec1f27" stroke-width="1"/><path d="M1.5 7 H12.5" stroke="#ec1f27" stroke-width="1"/></svg>
        www.vellutoevents.com.au
      </li>
      <li class="social">
        <span class="social-square"></span>
        Velluto Events
      </li>
    </ul>
  </section>
</main>
</body>
</html>
```